Law Firm
To All Designers:
New e-mail address for the project is daniel@rvestlegal.net.
Thanks. I love all the designs.
P.S. I like the orange on the one side of the card as opposed to black.
@ph - New drafts #161 & #162 in lieu of 145 & 146 are submitted, Can you please check & provide feedback in private message.
Thanks
draft #145 and #146 Drafts came out black and I cannot see them (look like negatives). Please resubmit. Thanks.
Please DO NOT PUT "Gavels", "Scales of Justice" "Court Buildings", etc. on the card. I DO NOT WANT IT.
Thanks.
draft #130 Card looks a lot better. Can I see it with the dot at the end of the big line through the card a little smaller (but that is the look I was going for) and can I see some color (black, orange and/or grey) below that line where the address, phone and e-mail appear? Also, can I see with just the "m" and the line part of the logo on the other side? Thanks.
draft #125 and #126 Looks better. I didn't like the "watermark" "m" in my logo being sideways on the card (it didn't look like an "m" anymore to me that way), but Ido like it on the stationary and envelope. Can I see the card with the same orange on the one side with the orange line under the "m" in my logo at the bottom of the card then the address, telephone and e-mail below it? Thanks.
To all designers,
Can I start seeing letterhead, envelopes, fax covers and e-mail signatures too! I look forward to seeing the designs!
draft #49 I like the line under my name like in the logo. Can I see with orange on the other side of the card?
drafts #101, #102, #103 and #104 I would like to see with orange on the other side of the card rather than black
I like the use of the whites and oranges with black accents. So not too much black. I also like orange with the logo (either with the text or just the script "m") on one side of the card. Thanks for all the great designs.
draft #35 I like the use of the logo at the bottom of the card. But "no "scales of justice", "court buildings" or "gavels", etc. was not something I wanted on the card, it was just an instruction to the designers that although I am a lawyer, I do not want to use these symbols.
draft #31 and #32 Maybe you could use the orange line under the script "m" under the logo for the "white space"?
draft #31 and #32 Like the use of the colors in the card and the "watermark" logo on the stationary. However, there is too much "white space" on the right side of the card. Other drafts did better job with "white space". I would also like to maybe see the "watermark" logo used in the card as well.

```html
<!DOCTYPE html>
<html lang="en">
<head>
<meta charset="utf-8">
<title>Daniel R. Vest P.C. – Business Card</title>
<link rel="stylesheet" href="https://fonts.googleapis.com/css2?family=Tinos:wght@400;700&display=swap">
<style>
  :root {
    --backdrop: #e4e4e6;
    --card: #ffffff;
    --ink: #262626;
    --muted: #444444;
    --orange: #ea5420;
    --rule: #c9c9c9;
  }
  * { box-sizing: border-box; margin: 0; padding: 0; }
  html, body { width: 1200px; height: 852px; overflow: hidden; }
  body {
    background: var(--backdrop);
    position: relative;
    font-family: "Tinos", "Times New Roman", serif;
    color: var(--ink);
  }
  .card {
    position: absolute;
    width: 560px;
    height: 320px;
    background: var(--card);
    border-radius: 22px;
    box-shadow: 0 6px 18px rgba(0,0,0,0.18);
    overflow: hidden;
  }
  .card--front { left: 60px; top: 70px; }
  .card--back  { left: 580px; top: 462px; }

  .edge-tab {
    position: absolute;
    width: 9px;
    background: var(--orange);
  }
  .edge-tab--right { right: 0; border-radius: 5px 0 0 5px; }
  .edge-tab--left  { left: 0;  border-radius: 0 5px 5px 0; }

  .firm-name {
    position: absolute;
    font-family: "Tinos", "Times New Roman", serif;
    font-weight: 400;
    color: var(--ink);
    white-space: nowrap;
    line-height: 1;
  }
  .card--front .firm-name { left: 0; right: 0; text-align: center; top: 92px; font-size: 36px; }
  .card--back .firm-name { left: 34px; top: 250px; font-size: 30px; }

  .divider {
    position: absolute;
    width: 1px;
    background: var(--rule);
  }

  .person__name {
    color: var(--orange);
    font-weight: 700;
    font-size: 18px;
    line-height: 1.2;
  }
  .person__title {
    font-size: 15px;
    color: var(--muted);
    line-height: 1.3;
  }
  .card--front .person { position: absolute; right: 275px; top: 192px; text-align: right; }
  .card--back  .person { position: absolute; left: 278px; top: 46px; }

  .contact {
    position: absolute;
    font-size: 14px;
    line-height: 18px;
    color: var(--muted);
  }
  .contact__address { margin-bottom: 9px; }
  .contact__row { display: flex; align-items: center; gap: 6px; }
  .contact__row svg { width: 11px; height: 11px; flex: none; }
  .card--front .contact { left: 316px; top: 192px; }
  .card--back  .contact { left: 278px; top: 114px; }
</style>
</head>
<body>

  <section class="card card--front" aria-label="Business card front">
    <div class="firm-name">Daniel R. Vest P.C.</div>

    <div class="edge-tab edge-tab--left" style="top:200px; height:70px;"></div>

    <div class="person">
      <div class="person__name">Daniel R. Vest</div>
      <div class="person__title">Principal</div>
    </div>

    <div class="divider" style="left:300px; top:186px; height:92px;"></div>

    <div class="contact">
      <div class="contact__address">18 Harlow Lane<br>Millbrook, NY 12545</div>
      <div class="contact__row">
        <svg viewBox="0 0 12 12" aria-hidden="true"><path fill="var(--orange)" d="M2.6 0.8l1.8 0 .8 2.4-1.2 .9c.6 1.3 1.6 2.3 2.9 2.9l.9-1.2 2.4 .8 0 1.8c0 .7-.6 1.2-1.2 1.1C5 9.2 1.6 5.8 1.5 2c0-.7.4-1.2 1.1-1.2z"/></svg>
        <span>(555) 014-2290</span>
      </div>
      <div class="contact__row">
        <svg viewBox="0 0 12 12" aria-hidden="true"><rect x="0.5" y="2" width="11" height="8" rx="1" fill="var(--orange)"/><path d="M1 2.6l5 3.8 5-3.8" fill="none" stroke="#fff" stroke-width="1"/></svg>
        <span>daniel@rvestlegal.net</span>
      </div>
    </div>

    <div class="edge-tab edge-tab--right" style="top:112px; height:92px;"></div>
  </section>

  <section class="card card--back" aria-label="Business card back">
    <div class="edge-tab edge-tab--right" style="top:40px; height:96px;"></div>
    <div class="edge-tab edge-tab--left" style="top:170px; height:96px;"></div>

    <div class="divider" style="left:262px; top:40px; height:162px;"></div>

    <div class="person">
      <div class="person__name">Daniel R. Vest</div>
      <div class="person__title">Principal</div>
    </div>

    <div class="contact">
      <div class="contact__address">18 Harlow Lane<br>Millbrook, NY 12545</div>
      <div class="contact__row">
        <svg viewBox="0 0 12 12" aria-hidden="true"><path fill="var(--orange)" d="M2.6 0.8l1.8 0 .8 2.4-1.2 .9c.6 1.3 1.6 2.3 2.9 2.9l.9-1.2 2.4 .8 0 1.8c0 .7-.6 1.2-1.2 1.1C5 9.2 1.6 5.8 1.5 2c0-.7.4-1.2 1.1-1.2z"/></svg>
        <span>(555) 014-2290</span>
      </div>
      <div class="contact__row">
        <svg viewBox="0 0 12 12" aria-hidden="true"><rect x="0.5" y="2" width="11" height="8" rx="1" fill="var(--orange)"/><path d="M1 2.6l5 3.8 5-3.8" fill="none" stroke="#fff" stroke-width="1"/></svg>
        <span>daniel@rvestlegal.net</span>
      </div>
    </div>

    <div class="firm-name">Daniel R. Vest P.C.</div>
  </section>

</body>
</html>
```